An animal window cleaning business card

I want a business card design that includes a logo and tells people I am a WINDOW WASHING COMPANY right away.
Were based in Maine, we do window cleaning, pressure washing, and gutter cleaning. We like Pine trees, the Ocean, state of Maine symbols, Lobsters, Moose, Huskies, etc. My business name is "BRIGHT PANE WINDOWS"
The card could also be designed to look like a gift credit card with a 50$ value.

Target Market(s)

my target audience is older folks with disposable money who live on the ocean or have secondary homes for vacation in Maine

Industry/Entity Type

Cleaning Services

Contact Information for Business Card

2.5x3" plastic if possible.

Font styles to use
Sans Serif

Requirements
Must have
• a symbol, or a logo that tells people I am a window washing company Instantly.
The words BRIGHT PANE, my phone number, my name, MY email
Nice to have
• a lobster holding a squeegee, or a stylized cartoonish version of a human huskie holding a squeegee,
Should not have
• a lighthouse
small hard to read text

```html
<!DOCTYPE html>
<html lang="en">
<head>
<meta charset="utf-8">
<title>Bright Pane Windows – Gift Card</title>
<link rel="stylesheet" href="https://fonts.googleapis.com/css2?family=Poppins:wght@400;500;600;700;800&display=swap">
<style>
  :root {
    --page-bg: #dfe7ef;
    --card-white: #ffffff;
    --ice: #d8eefb;
    --sky: #7cc4f0;
    --ocean: #2b87cf;
    --deep: #1668b2;
    --navy: #0f3f8c;
    --ink: #1b3f8f;
    --mascot-blue: #6a8fc4;
    --mascot-grey: #b9c3cf;
    --text-light: #ffffff;
  }
  * { box-sizing: border-box; margin: 0; padding: 0; }
  html, body { width: 1200px; height: 900px; overflow: hidden; }
  body {
    background: var(--page-bg);
    font-family: "Poppins", sans-serif;
    position: relative;
  }
  .gift-card {
    position: absolute;
    left: 225px; top: 236px;
    width: 750px; height: 428px;
    border-radius: 28px;
    overflow: hidden;
    background: linear-gradient(160deg, var(--card-white) 30%, var(--ice) 100%);
    box-shadow: 0 14px 40px rgba(20, 50, 90, .18);
  }
  .card-shapes { position: absolute; inset: 0; }
  .network-name {
    position: absolute; left: 24px; top: 20px;
    font-weight: 700; font-size: 22px; letter-spacing: .5px;
    color: var(--ink);
  }
  .mascot-art {
    position: absolute; left: 28px; top: 58px;
    width: 170px; height: 340px;
    border-radius: 60px 60px 14px 14px;
    background: linear-gradient(180deg, var(--mascot-grey) 0%, var(--mascot-blue) 55%, var(--navy) 100%);
    opacity: .85;
  }
  .brand-name {
    position: absolute; left: 178px; top: 205px;
    width: 240px;
    font-weight: 800; font-size: 44px; line-height: 1;
    color: var(--ink);
    text-align: center;
  }
  .brand-name .brand-sub { display: block; font-size: 28px; margin-top: 8px; letter-spacing: 1px; }
  .card-value {
    position: absolute; right: 32px; top: 22px;
    text-align: center; color: var(--text-light);
  }
  .card-value .amount { font-weight: 700; font-size: 46px; line-height: 1; letter-spacing: 1px; }
  .card-value .expiry { font-weight: 500; font-size: 9px; letter-spacing: .3px; margin-top: 4px; }
  .holder {
    position: absolute; right: 32px; top: 274px;
    text-align: right; color: var(--text-light);
  }
  .holder-name { font-weight: 600; font-size: 20px; line-height: 1.2; }
  .holder-title { font-weight: 500; font-size: 16px; line-height: 1.4; }
  .contact-list { list-style: none; margin-top: 14px; }
  .contact-list li {
    display: flex; justify-content: flex-end; align-items: center; gap: 8px;
    font-size: 17px; line-height: 1.45;
  }
  .contact-list svg { width: 14px; height: 14px; fill: var(--text-light); }
</style>
</head>
<body>
  <div class="gift-card">
    <svg class="card-shapes" viewBox="0 0 750 428" preserveAspectRatio="none" aria-hidden="true">
      <defs>
        <linearGradient id="ocean-fill" x1="0" y1="0" x2="0.3" y2="1">
          <stop offset="0" stop-color="#6fbcec"/>
          <stop offset="1" stop-color="#1a72bd"/>
        </linearGradient>
      </defs>
      <path d="M330 0 C420 90 430 300 360 428 L750 428 L750 0 Z" fill="#bfe3f8"/>
      <path d="M372 0 C455 100 460 300 390 428 L750 428 L750 0 Z" fill="#0f3f8c"/>
      <path d="M395 0 C475 105 478 300 405 428 L750 428 L750 0 Z" fill="url(#ocean-fill)"/>
      <path d="M540 0 C555 95 650 145 750 145 L750 0 Z" fill="#0f3f8c" stroke="#ffffff" stroke-width="5"/>
    </svg>

    <div class="network-name">NOVAPAY</div>

    <div class="mascot-art" role="img" aria-label="Cartoon husky window cleaner in overalls holding a squeegee and pressure washer wand"></div>

    <div class="brand-name">BRIGHT PANE<span class="brand-sub">WINDOWS</span></div>

    <div class="card-value">
      <div class="amount">50$</div>
      <div class="expiry">VALID THRU 06/2029</div>
    </div>

    <div class="holder">
      <div class="holder-name">EVAN HOLLIS</div>
      <div class="holder-title">MANAGING DIRECTOR</div>
      <ul class="contact-list">
        <li>207-555-0148
          <svg viewBox="0 0 24 24"><path d="M6.6 10.8a15.1 15.1 0 0 0 6.6 6.6l2.2-2.2c.3-.3.7-.4 1-.2 1.1.4 2.3.6 3.6.6.6 0 1 .4 1 1V20c0 .6-.4 1-1 1A17 17 0 0 1 3 4c0-.6.4-1 1-1h3.5c.6 0 1 .4 1 1 0 1.3.2 2.5.6 3.6.1.3 0 .7-.2 1z"/></svg>
        </li>
        <li>evan@brightpanemail.com
          <svg viewBox="0 0 24 24"><path d="M2 5h20v14H2z M2 5l10 8 10-8" fill="#ffffff" stroke="#1a72bd" stroke-width="1.6"/></svg>
        </li>
      </ul>
    </div>
  </div>
</body>
</html>
```